Redesign of Smart Watch Gift Voucher-SEE ATTACHED CURRENT DESIGN

I need to redesign my existing design using all same content and elements.

MY ENVISION: I invision more of a professional advertisement type of flyer/voucher. Imagine how Quorrel.com would create a professionally looking flyer promoting the tavix or tavun.

you can get many ideas about professional design by looking at some of quorrels flyer designs :
https://www.findlery.example/search?q=tavix+advertisment&tbm=isch

stock photos are attached, you do not have to use them all, you can use some or none i am open to your designs using your own images if you want...just make sure the smartwatch looks black

DO NOT LEAVE ANY CONTENT OR ELEMENTS OUT ON MOCK UP PLEASE

SEE ATTACHED CURRENT DESIGN

I need to redesign my existing design using all same content and elements. DO NOT LEAVE ANY CONTENT OR ELEMENTS OUT ON MOCK UP PLEASE

Target Market(s)

B2B-you can get many ideas about professional design by looking at some of quorrels flyer designs :

Industry/Entity Type

Marketing

Requirements
Must have
• I need to redesign my existing design using all same content and elements. DO NOT LEAVE ANY CONTENT OR ELEMENTS OUT ON MOCK UP PLEASE

Nice to have

Should not have

```html
<!DOCTYPE html>
<html lang="en">
<head>
<meta charset="UTF-8">
<title>Smartwatch Reward Voucher</title>
<link href="https://fonts.googleapis.com/css2?family=Montserrat:wght@400;500;700;800;900&family=Lato:wght@400;700&family=Barlow:wght@400&display=swap" rel="stylesheet">
<style>
  :root {
    --backdrop: #e9eaec;
    --paper: #ffffff;
    --paper-shade: #eef0f2;
    --ink: #222222;
    --ink-soft: #444444;
    --headline-grey: #555555;
    --brand-red: #e8202a;
    --brand-orange: #f7a41d;
    --tab-dark: #3a3a3c;
    --quote-grey: #cfd0d2;
    --rule-grey: #6a6a6a;
  }
  * { margin: 0; padding: 0; box-sizing: border-box; }
  html, body { width: 970px; height: 1200px; overflow: hidden; background: var(--backdrop); }
  .flyer {
    position: absolute; left: 21px; top: 0;
    width: 981px; height: 1269px;
    transform: scale(0.9456); transform-origin: top left;
    background: linear-gradient(160deg, var(--paper) 0%, var(--paper) 55%, var(--paper-shade) 100%);
    overflow: hidden;
    font-family: 'Lato', sans-serif;
    color: var(--ink);
  }
  .abs { position: absolute; }
  .swoosh { left: 0; top: 0; width: 981px; height: 1269px; }
  .hero-photo { right: 0; top: 0; width: 520px; height: 600px; }
  .side-photo { left: 28px; width: 280px; }
  .side-photo--sleeve { top: 540px; height: 230px; }
  .side-photo--charging { top: 790px; height: 290px; }

  .headline-enjoy {
    left: 44px; top: 38px;
    font-family: 'Montserrat', sans-serif; font-weight: 900;
    font-size: 150px; line-height: 150px; letter-spacing: 2px;
    background: linear-gradient(180deg, var(--brand-orange) 0%, #f26a22 55%, var(--brand-red) 100%);
    -webkit-background-clip: text; background-clip: text; color: transparent;
  }
  .headline-sub {
    left: 48px; top: 178px;
    font-family: 'Montserrat', sans-serif; font-weight: 800;
    font-size: 56px; line-height: 60px; color: var(--headline-grey);
  }
  .headline-product {
    left: 46px; top: 234px;
    font-family: 'Montserrat', sans-serif; font-weight: 900;
    font-size: 67px; line-height: 70px; color: var(--brand-red);
  }
  .rule { left: 48px; width: 476px; height: 3px; background: var(--rule-grey); }
  .tagline {
    left: 48px; top: 337px;
    font-family: 'Montserrat', sans-serif; font-weight: 400;
    font-size: 24px; line-height: 29px; color: var(--ink-soft);
  }
  .intro {
    left: 48px; top: 432px; width: 585px;
    font-family: 'Barlow', sans-serif; font-size: 16.5px; line-height: 21px; color: var(--ink-soft);
  }
  .tab {
    top: 594px; height: 34px; color: #fff;
    font-family: 'Montserrat', sans-serif; font-weight: 800; font-size: 19px; line-height: 34px;
  }
  .tab--features { left: 333px; width: 170px; padding-left: 20px; background: var(--brand-red); border-radius: 0 0 28px 0; }
  .tab--how { left: 601px; width: 324px; padding-left: 17px; background: var(--tab-dark); border-radius: 0 0 28px 0; }
  .feature-list { left: 352px; top: 637px; list-style: none; }
  .feature-list li { font-size: 18.5px; font-weight: 700; line-height: 23.1px; color: #2b2b2b; padding-left: 20px; position: relative; }
  .feature-list li::before { content: ""; position: absolute; left: 2px; top: 10px; width: 6px; height: 6px; border-radius: 50%; background: #2b2b2b; }
  .how-copy { left: 618px; top: 637px; width: 310px; font-size: 18.5px; line-height: 23.1px; color: var(--ink); }
  .quote-mark { top: 950px; width: 110px; height: 80px; }
  .quote-mark--open { left: 322px; }
  .quote-mark--close { left: 818px; }
  .testimonial { left: 420px; top: 953px; width: 410px; text-align: center; font-size: 18.5px; line-height: 23.1px; color: var(--ink); }

  .voucher { left: 57px; top: 1070px; width: 869px; height: 150px; border: 2px dashed #333; }
  .voucher-divider { left: 269px; top: 1095px; height: 108px; border-left: 2px dashed #333; }
  .voucher-meta { left: 57px; top: 1089px; width: 212px; text-align: center; font-family: 'Montserrat', sans-serif; font-size: 19px; line-height: 23px; }
  .voucher-meta .value { color: var(--brand-red); font-weight: 700; }
  .voucher-meta .label + .value { margin-bottom: 23px; }
  .voucher-cta { left: 272px; top: 1087px; width: 654px; text-align: center; font-family: 'Montserrat', sans-serif; }
  .voucher-cta .lead { font-size: 21px; font-weight: 500; line-height: 26px; letter-spacing: 0.5px; }
  .voucher-cta .url { font-size: 28.5px; font-weight: 800; line-height: 36px; margin-top: 3px; color: #111; }
  .voucher-cta .terms { font-size: 16.5px; font-weight: 500; line-height: 22px; margin-top: 2px; }
</style>
</head>
<body>
<div class="flyer">
  <svg class="abs swoosh" viewBox="0 0 981 1269" aria-hidden="true">
    <path d="M160 540 C 360 760, 330 1020, 330 1269" fill="none" stroke="#f2f3f5" stroke-width="30"/>
    <path d="M0 1200 C 300 1180, 700 1210, 981 1160 L981 1269 L0 1269 Z" fill="#f5f6f7"/>
  </svg>

  <svg class="abs hero-photo" viewBox="0 0 520 600" role="img" aria-label="Photo: hand with a black smartwatch showing a heart-rate screen">
    <defs>
      <linearGradient id="heroTone" x1="0" y1="0" x2="1" y2="1">
        <stop offset="0" stop-color="#8a96a6"/>
        <stop offset="0.4" stop-color="#d9a98a"/>
        <stop offset="0.75" stop-color="#2d3440"/>
        <stop offset="1" stop-color="#1b2230"/>
      </linearGradient>
    </defs>
    <path d="M150 0 L520 0 L520 600 L470 560 L430 480 L300 450 L180 430 L60 380 L100 330 L70 250 L130 200 L110 120 L150 60 Z" fill="url(#heroTone)"/>
  </svg>

  <svg class="abs side-photo side-photo--sleeve" viewBox="0 0 280 230" role="img" aria-label="Photo: wrist with a white smartwatch and plaid sleeve">
    <defs>
      <linearGradient id="sleeveTone" x1="0" y1="0" x2="1" y2="1">
        <stop offset="0" stop-color="#8a9aa8"/>
        <stop offset="0.6" stop-color="#c9b3a5"/>
        <stop offset="1" stop-color="#d8dde2"/>
      </linearGradient>
    </defs>
    <path d="M20 40 L100 0 L200 30 L260 90 L250 180 L200 225 L90 200 L0 120 Z" fill="url(#sleeveTone)"/>
  </svg>

  <svg class="abs side-photo side-photo--charging" viewBox="0 0 280 290" role="img" aria-label="Photo: black smartwatch with blue charging screen">
    <defs>
      <linearGradient id="chargeTone" x1="0" y1="0" x2="1" y2="1">
        <stop offset="0" stop-color="#e8eaee"/>
        <stop offset="0.5" stop-color="#3d6fb3"/>
        <stop offset="1" stop-color="#22252b"/>
      </linearGradient>
    </defs>
    <path d="M30 20 L150 0 L250 60 L270 170 L220 260 L120 290 L40 240 L0 130 Z" fill="url(#chargeTone)"/>
  </svg>

  <div class="abs headline-enjoy">ENJOY</div>
  <div class="abs headline-sub">YOUR BRAND NEW</div>
  <div class="abs headline-product">SMARTWATCH</div>

  <div class="abs rule" style="top:327px"></div>
  <div class="abs tagline">TAKE CONTROL OF YOUR LIFE WITH<br>YOUR NEW SMART FITNESS WATCH</div>
  <div class="abs rule" style="top:404px"></div>

  <p class="abs intro">Congratulations, you have been rewarded with a Brand New Smart Fitness Watch shipped right to your door. Just pay shipping and handling. Your new Smart Fitness Watch has these features: sport mode, pedometer, distance, calorie, heart rate, blood pressure, stopwatch, sleep monitoring, phone locator, reminders, remote camera, an alarm clock and much more!</p>

  <div class="abs tab tab--features">FEATURES</div>
  <ul class="abs feature-list">
    <li>Pedometer</li>
    <li>Calorie Counter</li>
    <li>Blood Pressure Monitor</li>
    <li>Sleep Monitoring</li>
    <li>Reminders Feature</li>
    <li>Alarm Clock</li>
    <li>Distance Tracker</li>
    <li>Heart Rate Monitor</li>
    <li>Stopwatch</li>
    <li>Phone Locator</li>
    <li>Remote Camera</li>
    <li>Waterproofv</li>
  </ul>

  <div class="abs tab tab--how">HOW CAN WE DO THIS?</div>
  <p class="abs how-copy">We have a couple retail partners that we team up with to "crowd purchase" huge shipping containers that hold 10's of thousands of electronic products at 80-90% off retail. We simply pass our savings on to you as we do not profit from our electronic products. You are basically able to "piggy back" on our partnerships and buying power to get an attractive electronic premium for a fraction of the retail cost.</p>

  <svg class="abs quote-mark quote-mark--open" viewBox="0 0 110 80" aria-hidden="true">
    <polygon points="20,0 55,0 35,75 0,75" fill="var(--quote-grey)"/>
    <polygon points="75,0 110,0 90,75 55,75" fill="var(--quote-grey)"/>
  </svg>
  <p class="abs testimonial">Are you sure this is not a Norvane Orbit Smartwatch in DISGUISE???? I love mine.<br>Corey T. Atlantic City, NJ</p>
  <svg class="abs quote-mark quote-mark--close" viewBox="0 0 110 80" aria-hidden="true">
    <polygon points="0,0 35,0 55,75 20,75" fill="var(--quote-grey)"/>
    <polygon points="55,0 90,0 110,75 75,75" fill="var(--quote-grey)"/>
  </svg>

  <div class="abs voucher"></div>
  <div class="abs voucher-divider"></div>
  <div class="abs voucher-meta">
    <div class="label">Certificate ID</div>
    <div class="value">91772-89218</div>
    <div class="label">Expires</div>
    <div class="value" style="margin-bottom:0">10/03/2020</div>
  </div>
  <div class="abs voucher-cta">
    <div class="lead">VIEW ALL THE DETAILS OF THIS SPECIAL OFFER<br>AND REDEEM ONLINE AT</div>
    <div class="url">WWW.REWARDSANDPERKSHUB.COM</div>
    <div class="terms">*Terms and Conditions apply see website for details</div>
  </div>
</div>
</body>
</html>
```